Flyer to Promote Membership in a Trade Association

UPDATE: I am looking for something modern and clean. NO CLIP ART. Not flashy. Just professional and modern. For everyone looking at our current flyer, we don't like it. That's why we aer looking for a new one. So please don't replicate it or use it as inspiration.

I need a flyer to promote membership in the Durable Residence Backers League. It can (probably should) be 2-sided. The content is attached as well as our logo and brand guidelines.

```html
<!DOCTYPE html>
<html lang="en">
<head>
<meta charset="utf-8">
<title>Join DRBL Today</title>
<link href="https://fonts.googleapis.com/css2?family=PT+Serif:wght@400;700&family=Fira+Sans:wght@500&family=Fira+Sans+Condensed:wght@500&family=Open+Sans:wght@400&display=swap" rel="stylesheet">
<style>
:root{
  --orange:#fa4f0b;
  --slate:#5b6670;
  --ink:#050505;
  --mist:#eff0ef;
  --white:#ffffff;
  --body:#4a5158;
}
*{box-sizing:border-box;margin:0;padding:0}
html,body{width:1200px;height:1200px;overflow:hidden;background:#f4f1ec}
.flyer{position:relative;width:1200px;height:1200px;background:var(--white);font-family:'Open Sans',sans-serif;color:var(--slate)}
.top-band{height:18px;background:var(--orange)}
.rule-heading{display:flex;align-items:center;gap:40px;font-family:'PT Serif',serif;font-weight:700;color:var(--slate);line-height:1}
.rule-heading::before,.rule-heading::after{content:"";flex:1;height:2px;background:var(--slate)}
.title{font-size:62px;margin-top:36px;height:64px}
.plans{display:flex;gap:20px;padding:0 48px 0 54px;margin-top:14px}
.plan{flex:1;height:236px;border-radius:20px;text-align:center;color:var(--white);padding-top:22px}
.plan--investor{background:var(--ink)}
.plan--affiliate{background:var(--slate)}
.plan-name{font-family:'PT Serif',serif;font-weight:700;font-size:36px;line-height:1.1}
.plan--investor .plan-name{color:var(--orange)}
.plan-who{font-family:'PT Serif',serif;font-size:15px;line-height:1.3;height:40px;margin-top:4px}
.plan-rule{width:68%;height:2px;background:var(--white);margin:18px auto 10px}
.plan-price{font-family:'Fira Sans',sans-serif;font-weight:500;font-size:25px;line-height:1.6}
.section{font-size:56px;margin-top:28px;height:58px}
.benefits{display:flex;padding:0 53px 0 44px;margin-top:14px;height:372px}
.benefit-col{flex:1;display:flex;flex-direction:column;gap:6px}
.divider{width:2px;background:var(--slate);margin:28px 62px 0}
.benefit h3{font-family:'PT Serif',serif;font-weight:700;font-size:20px;line-height:1.2;color:var(--slate);margin:0 0 2px 5px}
.benefit p{background:var(--mist);font-size:11.6px;line-height:1.35;padding:5px 20px 5px 6px;color:var(--body);min-height:48px}
.members-heading{font-size:34px;margin-top:4px;height:36px}
.roster{width:100%;border-collapse:collapse;margin-top:6px;font-family:'Fira Sans Condensed',sans-serif;font-weight:500;font-size:12.5px;color:var(--slate)}
.roster tr{height:21px}
.roster tr:nth-child(odd){background:var(--mist)}
.roster td{padding:0;width:17%}
.roster td:first-child{padding-left:104px;width:28%}
.footer{position:absolute;left:0;right:0;bottom:25px;height:106px;background:var(--ink);display:flex;align-items:center;justify-content:center;gap:24px;font-family:'PT Serif',serif;font-weight:700;font-size:44px}
.footer .ask{color:var(--orange)}
.footer .site{color:var(--slate)}
.base-band{position:absolute;left:0;right:0;bottom:0;height:25px;background:var(--slate)}
</style>
</head>
<body>
<main class="flyer">
  <div class="top-band"></div>
  <h1 class="rule-heading title">Join DRBL Today</h1>

  <section class="plans">
    <div class="plan plan--investor">
      <h2 class="plan-name">Investor Members</h2>
      <p class="plan-who">Banks, Insurance Companies,<br>Economic Investors</p>
      <div class="plan-rule"></div>
      <p class="plan-price">$5,000/year (assets≥$5B)<br>$1,000/year (assets &lt;$5B)</p>
    </div>
    <div class="plan plan--affiliate">
      <h2 class="plan-name">Affiliate Members</h2>
      <p class="plan-who">Syndicators &amp; Brokers</p>
      <div class="plan-rule"></div>
      <p class="plan-price">$4,500/year</p>
    </div>
  </section>

  <h2 class="rule-heading section">Member Benefits</h2>

  <section class="benefits">
    <div class="benefit-col">
      <div class="benefit"><h3>Members Only Conferences</h3><p>Two annual in-person meetings. Spring Meeting: investors-only for candid peer conversations. Fall Summit: full ecosystem gathering with syndicators and brokers.</p></div>
      <div class="benefit"><h3>Peer to Peer Meetups</h3><p>Find your peers—underwriters, asset managers, credit officers and more—with our meetups.</p></div>
      <div class="benefit"><h3>Searchable Member Directory</h3><p>Find underwriters, asset managers, and credit officers—searchable by role, firm type, and investment approach.</p></div>
      <div class="benefit"><h3>Shape Industry Standards<br>[ INVESTOR ONLY]</h3><p>DRBL's underwriting and asset management standards are adopted industry-wide. Influence them through our committees.</p></div>
    </div>
    <div class="divider"></div>
    <div class="benefit-col">
      <div class="benefit"><h3>Investor Only Forums</h3><p>Exclusive meetings and webinars for investors only, enabling candid conversations and meaningful collaboration.</p></div>
      <div class="benefit"><h3>Live &amp; On Demand Webinars</h3><p>Free monthly Third Thursday webinars covering Year 15 issues, secondary transactions, securitizing developer fees and other emerging topics.</p></div>
      <div class="benefit"><h3>Emerging Leaders Program<br>[INVESTOR ONLY]</h3><p>Develop your firm's next-generation leaders through dedicated professional development programming.</p></div>
    </div>
  </section>

  <h2 class="rule-heading members-heading">Our Investor Members Include</h2>
  <table class="roster">
    <tr><td>Larkmoor Life/Vantis Health</td><td>Tessaly Financial</td><td>Plain Citizens Bank</td><td>Old Harbor Life</td><td>Prentiss Holloway</td></tr>
    <tr><td>Corvel Bank</td><td>Keystead One</td><td>Ashgrove Partners</td><td>Solvane (ETRA)</td><td>RN Bank</td></tr>
    <tr><td>Meridian Crest National Bank</td><td>Everton Ridge Bank</td><td>Loyal Community Capital</td><td>QRT Real Estate</td><td>HamletBank</td></tr>
    <tr><td>Bank of Halvern</td><td>NWBC</td><td>Whitcombe Varley</td><td>Districts Affordable Housing</td><td>LatchBank</td></tr>
    <tr><td>Orlen Hartley Bank</td><td>Sevenfold CDC</td><td>Broadfield Insurance</td><td>Valdoro Bank</td><td>QVT Bank USA</td></tr>
    <tr><td>FSMA</td><td>Northgate Impact Finance</td><td>Harrow</td><td>Lane Bank</td><td></td></tr>
  </table>

  <footer class="footer"><span class="ask">Ready to join?</span><span class="site">drbl.org</span></footer>
  <div class="base-band"></div>
</main>
</body>
</html>
```